Detail Shop Business card design

i need a business card design for my new detailing company called 'Brenner's Detail Shop'. i want an all black and white design . simple, direct and to the point. i want the designer to choose a fitting font to match the logothe front should have logo, address, phone and email and the back side should have a slogan and text indicating that we offer services on anything including cars, trucks, motorcycles and RVs. slogan will read "we take pride in your ride"
maybe also very small on the back side the IG icon with Brenners_Detail_Shop

phone 482.615.7734
address 7384 E Harlow Ave
Spokane WA 99342
email: BrennersDetail@quorvail.com

Target Market(s)

all ages , auto enthusiasts

Industry/Entity Type

Automotive

Contact Information for Business Card

the front should have logo, address, phone and email and the back side should have a slogan and text indicating that we offer services on anything including cars, trucks, motorcycles and RVs. slogan will read "we take pride in your ride"

phone 482.615.7734
address 7384 E Harlow Ave
Spokane WA 99342

Colors
000000
ffffff

Requirements
Must have
• bold font and very simple design with good spacing
Nice to have
• anything creative from the designer indicating we service any types of vehicles
Should not have
• any colors ,

```html
<!DOCTYPE html>
<html lang="en">
<head>
<meta charset="utf-8">
<title>Brenner's Detail Shop — Business Card</title>
<link rel="stylesheet" href="https://fonts.googleapis.com/css2?family=Gelasio:ital,wght@0,400;0,700;1,400&display=swap">
<style>
  :root {
    --page: #ffffff;
    --card: #1b202e;
    --card-faint: #222838;
    --ink: #ffffff;
    --ink-soft: #d9dce3;
    --gold: #c9a43a;
  }
  html, body {
    margin: 0;
    width: 1200px;
    height: 1200px;
    overflow: hidden;
    background: var(--page);
  }
  .canvas {
    position: relative;
    width: 1200px;
    height: 1200px;
    font-family: "Gelasio", Georgia, serif;
    color: var(--ink);
  }
  .card {
    position: absolute;
    background: var(--card);
    overflow: hidden;
  }
  .card--front { left: 198px; top: 94px; width: 802px; height: 459px; }
  .card--back  { left: 202px; top: 649px; width: 788px; height: 449px; }

  /* Front: brand lockup */
  .brand {
    position: absolute;
    left: 0; right: 0;
    top: 120px;
    display: flex;
    flex-direction: column;
    align-items: center;
    gap: 14px;
  }
  .brand__mark {
    width: 64px; height: 64px;
    border-radius: 50%;
    border: 3px solid var(--ink);
    box-sizing: border-box;
  }
  .brand__name {
    font-size: 46px;
    font-weight: 700;
    letter-spacing: 0.5px;
    color: var(--ink);
    white-space: nowrap;
  }

  /* Front: contact row */
  .contact {
    position: absolute;
    left: 48px; right: 30px;
    top: 352px;
    display: flex;
    align-items: flex-start;
    font-style: italic;
    font-size: 16px;
    line-height: 22px;
    color: var(--ink);
  }
  .contact__item {
    display: flex;
    align-items: flex-start;
    gap: 10px;
    white-space: nowrap;
  }
  .contact__icon { width: 16px; height: 16px; margin-top: 3px; flex: none; }
  .contact__divider {
    width: 3px; height: 30px;
    background: var(--ink);
    margin: -2px 20px 0;
    flex: none;
  }

  /* Back */
  .watermark {
    position: absolute;
    left: 0; right: 0;
    top: 150px;
    text-align: center;
    font-size: 64px;
    font-weight: 700;
    color: var(--card-faint);
    white-space: nowrap;
  }
  .slogan {
    position: absolute;
    left: 0; right: 0;
    top: 176px;
    text-align: center;
    font-style: italic;
    font-size: 52px;
    color: var(--ink);
    white-space: nowrap;
  }
  .social {
    position: absolute;
    left: 20px;
    bottom: 20px;
    display: flex;
    align-items: center;
    gap: 6px;
    font-size: 10px;
    font-weight: 700;
    color: var(--ink);
  }
  .social__square {
    width: 17px; height: 17px;
    border: 2px solid var(--ink);
    box-sizing: border-box;
    border-radius: 3px;
  }
  .signoff {
    position: absolute;
    right: 82px;
    bottom: 40px;
    font-size: 34px;
    color: var(--gold);
  }
</style>
</head>
<body>
<main class="canvas">

  <section class="card card--front" aria-label="Card front">
    <div class="brand">
      <span class="brand__mark" aria-hidden="true"></span>
      <span class="brand__name">Brenner's Detail Shop</span>
    </div>

    <div class="contact">
      <div class="contact__item">
        <svg class="contact__icon" viewBox="0 0 24 24" fill="none" stroke="currentColor" stroke-width="1.6" aria-hidden="true">
          <path d="M5 3h4l2 5-2.5 1.5a11 11 0 0 0 6 6L16 13l5 2v4a2 2 0 0 1-2 2A17 17 0 0 1 3 5a2 2 0 0 1 2-2z"/>
        </svg>
        <span>482.615.7734</span>
      </div>
      <span class="contact__divider"></span>
      <div class="contact__item">
        <svg class="contact__icon" viewBox="0 0 24 24" fill="none" stroke="currentColor" stroke-width="1.6" aria-hidden="true">
          <rect x="3" y="6" width="18" height="13" rx="1"/>
          <path d="M3 7l9 7 9-7"/>
        </svg>
        <span>BrennersDetail@quorvail.com</span>
      </div>
      <span class="contact__divider"></span>
      <div class="contact__item">
        <svg class="contact__icon" viewBox="0 0 24 24" fill="none" stroke="currentColor" stroke-width="1.6" aria-hidden="true">
          <path d="M12 22s7-7 7-12a7 7 0 0 0-14 0c0 5 7 12 7 12z"/>
          <circle cx="12" cy="10" r="2.5"/>
        </svg>
        <span>7384 E Harlow Ave Spokane<br>WA 99342</span>
      </div>
    </div>
  </section>

  <section class="card card--back" aria-label="Card back">
    <div class="watermark" aria-hidden="true">Brenner's Detail Shop</div>
    <p class="slogan">“we take pride in your ride”</p>
    <div class="social">
      <span class="social__square" aria-hidden="true"></span>
      <span>@Brenners_Detail_Shop</span>
    </div>
    <div class="signoff">Brenner's</div>
  </section>

</main>
</body>
</html>
```